Website design that will showcase a medical assistance tool

I want the medical assistance tool (for hearing aids) website to have a premium or upmarket feel. The brand is Vorquelin (as per attached logo image for guidance). I want the website to appeal to both end users as well as hearing aid clinics.

```html
<!DOCTYPE html>
<html lang="en">
<head>
<meta charset="utf-8">
<title>Vorquelin — Hearing Aid Comfort &amp; Care</title>
<link rel="stylesheet" href="https://fonts.googleapis.com/css2?family=Montserrat:wght@400;500;600;700&display=swap">
<style>
:root{
  --beige:#c9c2a8;
  --beige-soft:#e8e4da;
  --beige-pale:#efece4;
  --grey-bg:#ebebeb;
  --footer-bg:#f1f1f1;
  --ink:#3f3f3f;
  --ink-soft:#5a5a5a;
  --white:#ffffff;
}
*{box-sizing:border-box;margin:0;padding:0}
html,body{width:1200px;height:4205px;overflow:hidden}
body{position:relative;font-family:"Montserrat",sans-serif;color:var(--ink);background:var(--white)}
.abs{position:absolute}
.section{position:absolute;left:0;width:1200px;overflow:hidden}
.btn{position:absolute;display:flex;align-items:center;justify-content:center;background:var(--beige);color:var(--white);border-radius:30px;font-size:13px;font-weight:600;letter-spacing:.04em}
.eyebrow{position:absolute;font-size:15px;letter-spacing:.3em;text-transform:uppercase;color:var(--ink)}
.title{position:absolute;font-weight:500;color:var(--ink-soft);line-height:1.1}
.body-copy{position:absolute;font-size:16px;line-height:25px;color:var(--ink)}
.placeholder{position:absolute}
.brand{display:flex;align-items:center;gap:8px;font-weight:500;color:#6b6b6b;text-transform:lowercase}
.brand-dot{border-radius:50%;background:var(--beige)}

/* header */
.site-header{top:0;height:72px;background:var(--white)}
.nav a{position:absolute;top:29px;font-size:13px;font-weight:500;color:var(--ink);text-decoration:none}

/* hero */
.hero{top:72px;height:633px;background:var(--grey-bg)}

/* about */
.about{top:705px;height:621px;background:var(--white)}

/* benefits */
.benefits{top:1326px;height:710px;background:var(--beige-soft)}
.card{position:absolute;top:168px;width:410px;height:461px;background:var(--white);border-radius:10px;overflow:hidden}
.card h3{position:absolute;left:58px;top:276px;font-size:21px;font-weight:600;color:var(--ink)}
.card .rule{position:absolute;left:58px;top:306px;width:38px;height:2px;background:var(--beige)}
.card ul{position:absolute;left:58px;top:324px;list-style:none}
.card li{display:flex;align-items:center;gap:8px;height:28px;font-size:14px;font-weight:500;color:var(--ink)}

/* technology */
.technology{top:2036px;height:590px;background:var(--white)}

/* steps */
.steps{top:2626px;height:561px;background:linear-gradient(100deg,var(--beige-soft),#efefef)}
.step{position:absolute;top:151px;width:326px;height:326px;border-radius:50%;background:var(--white);border:3px solid #dcdcdc;box-shadow:0 0 0 6px rgba(255,255,255,.6);text-align:center}
.step .num{margin-top:50px;font-size:62px;font-weight:400;color:var(--beige)}
.step h4{margin-top:6px;font-size:14px;font-weight:600;color:var(--ink)}
.step p{margin:6px auto 0;width:230px;font-size:12.5px;line-height:21px;color:var(--ink)}
.step.active{background:var(--beige);border-color:var(--beige)}
.step.active .num,.step.active h4,.step.active p{color:var(--white)}

/* testimonials */
.testimonials{top:3187px;height:627px;background:var(--white)}
.quote-side{position:absolute;top:250px;height:185px;background:#f6f6f6;border-radius:10px;font-size:11px;line-height:16px;color:#c5c5c5;text-align:center;padding:48px 30px}
.quote-main{position:absolute;left:274px;top:201px;width:644px;height:275px;background:var(--beige);border-radius:6px;text-align:center;color:var(--white)}
.quote-mark{position:absolute;left:534px;top:178px;font-size:110px;line-height:1;height:80px;overflow:hidden;color:var(--white);font-family:Georgia,serif}
.arrow-btn{position:absolute;top:3690px;width:46px;height:46px;border-radius:50%;background:var(--beige);display:flex;align-items:center;justify-content:center}

/* footer */
.site-footer{top:3814px;height:391px;background:var(--footer-bg)}
.footer-title{position:absolute;top:72px;font-size:18px;font-weight:600;color:var(--ink)}
.footer-links{position:absolute;top:110px;list-style:none}
.footer-links li{font-size:13px;line-height:22.5px;color:var(--ink-soft)}
.contact-item{position:absolute;left:599px;display:flex;align-items:center;gap:10px;font-size:12px;line-height:16px;color:var(--ink)}
.contact-icon{width:28px;height:28px;border-radius:50%;background:var(--beige);display:flex;align-items:center;justify-content:center;flex:none}
.social{position:absolute;top:172px;width:28px;height:28px;border-radius:50%;background:#8a8a8a}
</style>
</head>
<body>

<header class="section site-header">
  <div class="abs brand" style="left:124px;top:14px;font-size:34px">
    <span class="brand-dot" style="width:40px;height:40px"></span>vorquelin
  </div>
  <span class="abs brand-dot" style="left:500px;top:12px;width:14px;height:14px"></span>
  <nav class="nav">
    <a style="left:487px">Home</a>
    <a style="left:570px">For Individuals</a>
    <a style="left:710px">For Clinics</a>
    <a style="left:824px">About</a>
    <a style="left:908px">Support</a>
  </nav>
  <div class="btn" style="left:997px;top:24px;width:103px;height:30px;font-weight:500;font-size:13px">Contact</div>
</header>

<section class="section hero">
  <div class="placeholder" role="img" aria-label="Soft flowing dotted wave pattern across the hero" style="left:0;top:220px;width:1200px;height:260px;background:linear-gradient(180deg,rgba(201,194,168,0) 0%,rgba(201,194,168,.35) 50%,rgba(201,194,168,0) 100%)"></div>
  <div class="eyebrow" style="left:0;width:1200px;top:52px;text-align:center">Welcome to Vorquelin</div>
  <h1 class="title" style="left:0;width:1200px;top:78px;text-align:center;font-size:46px;line-height:49px">A New Standard in<br><span style="font-weight:600">Hearing Aid Comfort &amp; Care</span></h1>
  <div class="btn" style="left:518px;top:189px;width:164px;height:39px;font-size:12px">TRY IT NOW
    <svg width="14" height="10" viewBox="0 0 14 10" style="margin-left:6px"><path d="M1 5h11M8 1l4 4-4 4" stroke="#fff" stroke-width="1.6" fill="none"/></svg></div>
  <div class="placeholder" role="img" aria-label="Gold behind-the-ear hearing aid with clear tube and dome set against a large beige curved shape" style="left:398px;top:254px;width:396px;height:396px;border-radius:50%;background:radial-gradient(circle at 40% 45%,#e9e2c9 0%,#cfc6a6 55%,#c4bb9b 100%)"></div>
  <div class="abs" style="left:599px;top:600px;width:1px;height:71px;background:#9a9a9a"></div>
</section>

<section class="section about">
  <div class="abs" style="left:88px;top:61px;width:460px;height:460px;border-radius:50%;background:var(--beige)"></div>
  <div class="placeholder" role="img" aria-label="Smiling senior man fitting a hearing aid behind his ear, with a beige hearing aid shown beside the portrait" style="left:108px;top:81px;width:440px;height:440px;border-radius:50%;background:linear-gradient(135deg,#d9d6d0,#9a8f9c 60%,#6f6a80)"></div>
  <div class="eyebrow" style="left:588px;top:107px;padding:2px 10px;background:var(--beige-soft);font-size:15px">About Vorquelin</div>
  <h2 class="title" style="left:593px;top:140px;font-size:42px;display:flex;align-items:center;gap:10px">About the Technology<span class="brand-dot" style="width:40px;height:40px"></span></h2>
  <p class="body-copy" style="left:596px;top:208px;width:520px">Lorem ipsum dolor sit amet, consectetur adipiscing elit, sed do eiusmod tempor incididunt ut labore et dolore magna aliqua. Quis ipsum suspendisse ultrices gravida. Risus commodo viverra maecenas accumsan lacus vel facilisis.</p>
  <p class="body-copy" style="left:596px;top:333px;width:520px">Lorem ipsum dolor sit amet, consectetur adipiscing elit, sed do eiusmod tempor incididunt ut labore et dolore magna aliqua. Quis ipsum suspendisse ultrices gravida.</p>
  <div class="btn" style="left:599px;top:433px;width:163px;height:44px">LEARN MORE</div>
</section>

<section class="section benefits">
  <div class="placeholder" role="img" aria-label="Soft dotted wave pattern behind the cards" style="left:0;top:330px;width:1200px;height:200px;background:linear-gradient(180deg,rgba(201,194,168,0),rgba(201,194,168,.35),rgba(201,194,168,0))"></div>
  <div class="eyebrow" style="left:477px;top:58px;padding:0 10px;background:var(--white);font-size:15px">Why Choose Us</div>
  <h2 class="title" style="left:0;width:1200px;top:85px;text-align:center;font-size:44px">Benefits &amp; Features</h2>
  <article class="card" style="left:173px">
    <div class="placeholder" role="img" aria-label="Smiling man with glasses touching a hearing aid behind his ear, greenery behind" style="left:0;top:0;width:410px;height:242px;background:linear-gradient(120deg,#3c4a3a,#8e9a86 55%,#c8cbbf)"></div>
    <h3>FOR END USERS</h3><div class="rule"></div>
    <ul>
      <li><svg width="14" height="10"><path d="M1 5l4 4 8-8" stroke="#b8b095" stroke-width="2" fill="none"/></svg>Comfort</li>
      <li><svg width="14" height="10"><path d="M1 5l4 4 8-8" stroke="#b8b095" stroke-width="2" fill="none"/></svg>Hygiene</li>
      <li><svg width="14" height="10"><path d="M1 5l4 4 8-8" stroke="#b8b095" stroke-width="2" fill="none"/></svg>Ease of use</li>
      <li><svg width="14" height="10"><path d="M1 5l4 4 8-8" stroke="#b8b095" stroke-width="2" fill="none"/></svg>Improved experience</li>
    </ul>
  </article>
  <article class="card" style="left:599px">
    <div class="placeholder" role="img" aria-label="Clinician fitting a hearing aid on a patient's ear" style="left:0;top:0;width:410px;height:242px;background:linear-gradient(120deg,#5a4a40,#a89a8c 50%,#e2e0de)"></div>
    <h3 style="left:70px">FOR CLINICS</h3><div class="rule" style="left:70px"></div>
    <ul style="left:70px">
      <li><svg width="14" height="10"><path d="M1 5l4 4 8-8" stroke="#b8b095" stroke-width="2" fill="none"/></svg>Increased patient satisfaction</li>
      <li><svg width="14" height="10"><path d="M1 5l4 4 8-8" stroke="#b8b095" stroke-width="2" fill="none"/></svg>Reduced follow-up issues</li>
      <li><svg width="14" height="10"><path d="M1 5l4 4 8-8" stroke="#b8b095" stroke-width="2" fill="none"/></svg>Premium positioning</li>
    </ul>
  </article>
  <div class="abs" style="left:555px;top:372px;width:70px;height:70px;border-radius:50%;background:var(--beige-soft);display:flex;align-items:center;justify-content:center"><span class="brand-dot" style="width:40px;height:40px;background:var(--white)"></span></div>
</section>

<section class="section technology">
  <div class="abs" style="left:588px;top:26px;width:570px;height:570px;border-radius:50%;background:var(--beige-pale)"></div>
  <div class="placeholder" role="img" aria-label="Smiling senior woman with grey hair adjusting a hearing aid behind her ear" style="left:620px;top:26px;width:510px;height:564px;border-radius:255px 255px 0 0;background:linear-gradient(160deg,#cfcac3,#b49a86 45%,#ece8e2 80%)"></div>
  <div class="eyebrow" style="left:126px;top:102px;font-size:15px">Why Choose Us</div>
  <h2 class="title" style="left:124px;top:128px;font-size:44px;line-height:47px">Technology &amp; <span class="brand-dot" style="display:inline-block;width:40px;height:40px;vertical-align:middle"></span><br>Design Excellence</h2>
  <p class="body-copy" style="left:133px;top:241px;width:420px">Lorem ipsum dolor sit amet, consectetur adipiscing elit, sed do eiusmod tempor incididunt ut labore et dolore magna aliqua Quis ipsum suspe</p>
  <p class="body-copy" style="left:133px;top:341px;width:420px">Lorem ipsum dolor sit amet, consectetur adipiscing elit, sed do eiusmod tempor incididunt.</p>
  <div class="btn" style="left:132px;top:417px;width:164px;height:42px">LEARN MORE</div>
</section>

<section class="section steps">
  <h2 class="title" style="left:0;width:1200px;top:52px;text-align:center;font-size:44px">How it Works</h2>
  <div class="step" style="left:152px"><div class="num">01</div><h4>Lorem ipsum dolor sit</h4><p>dipiscing elit, sed do eiusmod tempor incididunt ut labore et dolore magna aliqua. Quis ipsum sus-pendisse ultrices gravida</p></div>
  <div class="step" style="left:746px"><div class="num">03</div><h4>Lorem ipsum dolor sit</h4><p>dipiscing elit, sed do eiusmod tempor incididunt ut labore et dolore magna aliqua. Quis ipsum sus-pendisse ultrices gravida</p></div>
  <div class="step active" style="left:440px"><div class="num">02</div><h4>Lorem ipsum dolor sit</h4><p>dipiscing elit, sed do eiusmod tempor incididunt ut labore et dolore magna aliqua. Quis ipsum sus-pendisse ultrices gravida</p></div>
</section>

<section class="section testimonials">
  <div class="eyebrow" style="left:0;width:1200px;top:58px;text-align:center;font-size:15px">Testimonials</div>
  <h2 class="title" style="left:0;width:1200px;top:83px;text-align:center;font-size:44px">What People are Saying</h2>
  <div class="quote-side" style="left:121px;width:200px;text-align:left">"Lorem ipsum dolor sit amet, eiusmod tempor incididunt ipsum suspendisse maecenas</div>
  <div class="quote-side" style="left:880px;width:190px;text-align:right">dipiscing elit, sed do magna aliqua. Quis commodo viverra facilisis"</div>
  <div class="quote-main">
    <p style="margin:76px auto 0;width:560px;font-size:18px;line-height:25px">“Lorem ipsum dolor sit amet, consectetur adipiscing elit, sed do eiusmod tempor incididunt ut labore et dolore magna aliqua. Quis ipsum suspendisse ultrices gravida. Risus commodo viverra maecenas accumsan lacus vel facilisis”</p>
    <p style="margin-top:14px;font-size:17px;font-weight:600">Marcus Thorne</p>
    <p style="margin-top:4px;font-size:16px;letter-spacing:5px">★★★★★</p>
    <span class="quote-mark">”</span>
  </div>
  <div class="placeholder" role="img" aria-label="Portrait of a smiling customer" style="left:549px;top:156px;width:98px;height:98px;border-radius:50%;border:3px solid var(--white);background:linear-gradient(135deg,#e6c9a4,#c9946e)"></div>
</section>
<div class="arrow-btn" style="left:550px"><svg width="14" height="14"><path d="M9 2L4 7l5 5" stroke="#fff" stroke-width="2" fill="none"/></svg></div>
<div class="arrow-btn" style="left:607px"><svg width="14" height="14"><path d="M5 2l5 5-5 5" stroke="#fff" stroke-width="2" fill="none"/></svg></div>

<footer class="section site-footer">
  <div class="abs brand" style="left:133px;top:58px;font-size:34px"><span class="brand-dot" style="width:40px;height:40px"></span>vorquelin</div>
  <p class="abs" style="left:141px;top:120px;width:240px;font-size:11.5px;line-height:19px;color:var(--ink)">Lorem ipsum dolor sit amet, consectetur adipiscing elit, sed do eiusmod tempor</p>
  <span class="social" style="left:141px"></span><span class="social" style="left:175px"></span><span class="social" style="left:210px"></span><span class="social" style="left:244px"></span>

  <h4 class="footer-title" style="left:413px">Navigation</h4>
  <ul class="footer-links" style="left:417px"><li>Home</li><li>For Individuals</li><li>For Clinics</li><li>About</li><li>Support</li><li>Contact</li></ul>

  <h4 class="footer-title" style="left:599px">Contact us</h4>
  <div class="contact-item" style="top:110px"><span class="contact-icon"><svg width="12" height="14"><path d="M6 13s5-5 5-8a5 5 0 0 0-10 0c0 3 5 8 5 8z" fill="#fff"/></svg></span>48 Harrowden Lane<br>Suite 12, Bristol, UK BS8 4QT</div>
  <div class="contact-item" style="top:156px"><span class="contact-icon"><svg width="12" height="12"><path d="M2 1l3 0 1 3-2 1a7 7 0 0 0 3 3l1-2 3 1 0 3c-6 0-9-3-9-9z" fill="#fff"/></svg></span>+44 (0)117 496 0372</div>
  <div class="contact-item" style="top:195px"><span class="contact-icon"><svg width="14" height="10"><rect x="1" y="1" width="12" height="8" fill="none" stroke="#fff" stroke-width="1.4"/><path d="M1 1l6 5 6-5" stroke="#fff" stroke-width="1.4" fill="none"/></svg></span>hello@vorquelin.com</div>

  <h4 class="footer-title" style="left:890px">Subscribe Newletter</h4>
  <div class="abs" style="left:893px;top:108px;width:201px;height:31px;border-radius:16px;background:var(--white);font-size:11px;color:var(--ink);padding:8px 20px">Email address</div>
  <div class="btn" style="left:893px;top:157px;width:201px;height:30px;font-size:11px;font-weight:500">Subscribe ↗</div>

  <div class="abs" style="left:134px;top:314px;width:952px;height:1px;background:var(--beige)"></div>
  <p class="abs" style="left:154px;top:339px;font-size:12px;color:var(--ink)">Copyright © 2025 vorquelin. All Right Reserved</p>
  <p class="abs" style="left:816px;top:339px;font-size:12px;color:var(--ink);word-spacing:2px">Terms of Use &nbsp;&nbsp; Privacy Policy &nbsp;&nbsp; Disclaimer</p>
</footer>

</body>
</html>
```